Zesty Closers Banner for website:

We are doing up a banner for a Zesty Closers Website on this wordpress theme: http://demo.quillframe.net/compact/
Our theme for Zesty closers is that - We exist to create enormously successful salespeople and savvy business people to take you them to the top!
Our logo is attached below and uses Trajan Font. You can either incorporate it or not (we don't mind either way as you see with the example banners they don't incorporate their logos at all).
We want the banner split into two sections, biggest part at the top with picture and this will also have writing in it which guides people to our newsletter (our main aim is to get people from the banner first look to sign up to our newsletter). The second part which is smaller will have the newsletter area/sign up.
Some favourite banners for ideas are:
- http://www.janetbrimwick.com/ - this this as what we want is similar to above, want to split ours like this to funnel people into our newsletter.
- www.bloomandbranchstudio.com.au - we like this one as it has a picture but also writing
- http://corinnevaldemar.com/ - quite like this banner as it comes across to a very similar target market and looks professional
Was thinking the words something around: Believe you can be the best....? Open to other ideas.
I can send some photos if you like, but thought you might like to see what you would want to do before any photos went out. We have attached logo below and a social media arrow slide that we thought looked quite cool but it would have to be adjusted to the words Sales in the circle and words like customers, profit, money, margin, products, services in arrows. Not a must have but just a thought??? You guys are the gurus you normally come up with something very cool.
Our target market is Corporate sales people and teams, businesses (both new and existing to improve sales) and new business owners starting up businesses (especially women on how to sell) but really anyone wanting to know how to sell!!!
- Two sections, one part for picture to sell the idea to sign up to our newsletter, the other part for newsletter sign up

```html
<!DOCTYPE html>
<html lang="en">
<head>
<meta charset="utf-8">
<title>Zesty Closers – Website Banner</title>
<link href="https://fonts.googleapis.com/css2?family=Cinzel:wght@400;700&family=Cabin:wght@600&family=Cabin+Condensed:wght@400;600&display=swap" rel="stylesheet">
<style>
  :root {
    --page: #ffffff;
    --sky: #1e8fdc;
    --deep: #1262b8;
    --panel-top: #2a86d6;
    --panel-bottom: #155fb3;
    --strip: #a9e6fb;
    --ink-white: #ffffff;
    --headline-ice: #dff3ff;
    --sketch: #cfe6fa;
    --label-grey: #4a6676;
    --field: #d8f3ff;
    --field-edge: #7fb2c8;
    --brand: #1f4fa0;
    --photo-light: #e8eef3;
    --photo-mid: #b9cbd8;
  }
  * { margin: 0; padding: 0; box-sizing: border-box; }
  html, body { width: 1200px; height: 901px; overflow: hidden; background: var(--page); }

  .banner {
    position: absolute; left: 13px; top: 179px; width: 1172px; height: 521px;
    background: var(--sky); overflow: hidden;
  }
  .hero {
    position: absolute; left: 0; top: 0; width: 1172px; height: 403px;
    background: linear-gradient(180deg, var(--sky) 0%, var(--deep) 100%);
  }
  .hero-panel {
    position: absolute; left: 23px; top: 25px; width: 1120px; height: 357px;
    background: linear-gradient(160deg, var(--panel-top) 0%, var(--panel-bottom) 100%);
    box-shadow: 0 0 0 1px rgba(255,255,255,0.08);
  }
  .hero-photo {
    position: absolute; left: 661px; top: 33px; width: 482px; height: 349px;
    background: linear-gradient(90deg, rgba(232,238,243,0) 0%, var(--photo-light) 26%, var(--photo-mid) 100%);
  }

  .headline {
    position: absolute; font-family: "Cinzel", serif; color: var(--headline-ice);
    text-shadow: 0 2px 3px rgba(0,40,90,0.35); line-height: 1; white-space: nowrap;
  }
  .headline-your { left: 49px; top: 58px; font-size: 50px; }
  .headline-business { left: 122px; top: 106px; font-size: 71px; font-weight: 700; letter-spacing: -1px; }
  .headline-must { left: 383px; top: 175px; font-size: 50px; }
  .headline-goon { left: 540px; top: 166px; font-size: 68px; font-weight: 700; letter-spacing: -3px; }

  .tagline {
    position: absolute; left: 60px; top: 236px; font-family: "Cabin Condensed", sans-serif;
    font-size: 30px; line-height: 38px; letter-spacing: 0.6px; color: var(--ink-white);
  }

  .diagram {
    position: absolute; left: 374px; top: 237px; width: 386px; height: 135px;
    background: radial-gradient(ellipse at 50% 60%, rgba(207,230,250,0.28) 0%, rgba(207,230,250,0.12) 45%, rgba(207,230,250,0) 72%);
  }

  .pointer { position: absolute; left: 198px; top: 362px; width: 220px; height: 70px; z-index: 2; }

  .signup {
    position: absolute; left: 0; top: 403px; width: 1172px; height: 118px;
    background: linear-gradient(180deg, #6fb8d6 0%, var(--strip) 12%, var(--strip) 100%);
  }
  .brand {
    position: absolute; left: 30px; top: 30px; display: flex; align-items: center; gap: 12px;
  }
  .brand-dot { width: 26px; height: 26px; border-radius: 50%; background: var(--brand); }
  .brand-name {
    font-family: "Cinzel", serif; font-weight: 700; font-size: 33px; color: var(--brand); white-space: nowrap;
  }
  .signup-prompt {
    position: absolute; left: 376px; top: 25px; font-family: "Cabin", sans-serif;
    font-weight: 600; font-size: 20px; letter-spacing: 0.3px; color: var(--label-grey); white-space: nowrap;
  }
  .field {
    position: absolute; top: 61px; width: 223px; height: 28px;
    background: linear-gradient(180deg, #eefaff 0%, var(--field) 100%);
    border: 1px solid var(--field-edge);
    font-family: "Cabin Condensed", sans-serif; font-size: 18px; color: #8aa3b0;
    padding: 2px 7px; line-height: 22px;
  }
  .field-name { left: 498px; }
  .field-email { left: 745px; }
  .submit {
    position: absolute; left: 1002px; top: 41px; width: 87px; height: 62px;
    background: linear-gradient(160deg, #ffffff 0%, #f1f5f7 70%, #cfd8dd 100%);
    border-radius: 4px 4px 14px 4px; box-shadow: 2px 3px 4px rgba(0,0,0,0.25);
    font-family: "Cinzel", serif; font-size: 24px; line-height: 23px; color: #111;
    text-align: center; padding-top: 7px;
  }
</style>
</head>
<body>
<section class="banner">
  <div class="hero">
    <div class="hero-panel"></div>
    <div class="hero-photo" role="img" aria-label="Photo of a smiling businesswoman with shoulder-length auburn hair in a bright office"></div>

    <div class="headline headline-your">Your</div>
    <div class="headline headline-business">Bussiness</div>
    <div class="headline headline-must">Must</div>
    <div class="headline headline-goon">GO ON</div>

    <p class="tagline">Your tag &amp; text here<br>your tag hereyour tag here<br>your tag here .....</p>

    <div class="diagram" role="img" aria-label="Hand-drawn social media sketch: a circle with arrows to share, research, comment, blog and promote"></div>
  </div>

  <div class="signup">
    <div class="brand">
      <span class="brand-dot"></span>
      <span class="brand-name">Zesty Closers</span>
    </div>
    <p class="signup-prompt">Subcribe now to get newsletter about how to sell your bussiness</p>
    <div class="field field-name">Name</div>
    <div class="field field-email">E-mail</div>
    <div class="submit">GET<br>IT!</div>
  </div>

  <svg class="pointer" viewBox="0 0 220 70" aria-hidden="true">
    <path d="M2 6 C 90 4, 160 18, 204 58" stroke="#ffffff" stroke-width="3" fill="none" stroke-linecap="round"/>
    <path d="M188 58 L206 61 L206 44" stroke="#ffffff" stroke-width="3" fill="none" stroke-linecap="round" stroke-linejoin="round"/>
  </svg>
</section>
</body>
</html>
```